Retail Appliance Store Chain needs NEW business Card

Name of my company is Brandon's Appliances brandonsappliances.com is our website. . We are a 2 location brick and mortar, and online store selling premium, luxury, and normal household appliances, such as ovens, stoves, cooktops, dishwashers, refrigerators, washers and dryers, grills, air conditioners etc. The focus is on large kitchen appliances and laundry appliances.
Please visit http://brandonsappliances.com to get a feel for the business and branding.
I have attached the Brandon's Appliances logo (i do not have eps or psd or ai). And I have also attached our current business cards that we use. We have two versions. A double sided version for managers, and a one side version for regular employees.
Please submit BOTH one sided and two sided designs if possible.
Please keep consistent with the Brandon's Appliances logo, colors, etc.
I would prefer no rounded corners on the business card designs for printing costs.
Information on the cards (in no particular order):
Name - Employee Name
Business name - Brandon's Appliances
website - brandonsappliances.com
Email - Employee Email
2 Phone Numbers - store 1 address, store 2 address
2 Addresses - store 1 address, store 2 address

*do NOT need Fax #

Industry/Entity Type

Home Appliance

Contact Information for Business Card

Logo - Brandons Appliances Logo
Name - Employee Name
Email - Employee Email

Please no rounded corners. Standard US Business Card Size please.

Font styles to use
Serif
Sans Serif

Requirements
Must have
• colors and design that somewhat match the feel of current logo and website
Should not have
• No rounded corners.
No non-traditional business card size. US Standard Business Card Size only

```html
<!DOCTYPE html>
<html lang="en">
<head>
<meta charset="utf-8">
<title>Brandon's Appliances — Business Card</title>
<link rel="stylesheet" href="https://fonts.googleapis.com/css2?family=Open+Sans:wght@400;700;800&display=swap">
<style>
  :root {
    --brand-blue: #15488a;
    --brand-blue-dark: #0f3a73;
    --photo-light: #3f6aa6;
    --photo-dark: #1a4583;
    --accent-grey: #6b6b6b;
    --paper: #ffffff;
    --backdrop: #2b2d31;
    --text-light: #ffffff;
  }
  * { box-sizing: border-box; margin: 0; padding: 0; }
  html, body {
    width: 1200px; height: 1000px; overflow: hidden;
    background: var(--backdrop);
    font-family: "Open Sans", Arial, sans-serif;
  }
  .canvas {
    width: 1200px; height: 1000px;
    display: flex; flex-direction: column; align-items: center; justify-content: center;
    gap: 44px;
  }
  .card {
    position: relative;
    width: 735px; height: 420px;
    overflow: hidden;
    box-shadow: 0 14px 30px rgba(0,0,0,0.45);
  }

  /* Front side */
  .card-front { background: var(--brand-blue); }
  .front-photo {
    position: absolute; inset: 0;
    background:
      linear-gradient(200deg, rgba(255,255,255,0.10) 0%, rgba(255,255,255,0) 45%),
      linear-gradient(120deg, var(--photo-dark) 0%, var(--photo-light) 50%, var(--photo-dark) 100%);
  }
  .front-wordmark {
    position: absolute; left: 0; right: 0; top: 50%;
    transform: translateY(-50%);
    text-align: center;
    color: var(--text-light);
    font-weight: 800;
    font-size: 50px;
    letter-spacing: 0.5px;
  }

  /* Back side */
  .card-back { background: var(--brand-blue); }
  .back-shape { position: absolute; inset: 0; }
  .contact {
    position: absolute; left: 58px; top: 48px;
    color: var(--text-light);
  }
  .contact-name {
    font-weight: 800; font-size: 25px; letter-spacing: 3px; text-transform: uppercase;
    line-height: 1.1;
  }
  .contact-title { font-size: 15px; margin-top: 2px; letter-spacing: 0.3px; }
  .addresses { margin-top: 24px; font-size: 15px; line-height: 1.35; letter-spacing: 0.3px; }
  .address-divider { width: 16px; height: 2px; background: var(--text-light); margin: 6px 0; }
  .channels { margin-top: 24px; list-style: none; font-size: 15px; line-height: 1.5; letter-spacing: 0.3px; }
  .channels li { display: flex; align-items: center; gap: 8px; }
  .channels svg { width: 13px; height: 13px; fill: var(--text-light); flex: none; }
  .back-wordmark {
    position: absolute; left: 395px; right: 20px; top: 180px;
    text-align: center;
    color: var(--brand-blue);
    font-weight: 800;
    font-size: 36px;
    letter-spacing: 0.3px;
  }
</style>
</head>
<body>
<main class="canvas">

  <section class="card card-front" aria-label="Card front">
    <div class="front-photo" role="img" aria-label="Photo of a modern kitchen with built-in ovens and bar stools, tinted blue"></div>
    <p class="front-wordmark">Brandon's Appliances</p>
  </section>

  <section class="card card-back" aria-label="Card back">
    <svg class="back-shape" viewBox="0 0 735 420" preserveAspectRatio="none" aria-hidden="true">
      <path d="M418 0 C 336 110, 318 290, 350 420 L735 420 L735 0 Z" fill="var(--accent-grey)"/>
      <path d="M440 0 C 358 110, 340 290, 374 420 L735 420 L735 0 Z" fill="var(--paper)"/>
    </svg>

    <div class="contact">
      <h1 class="contact-name">Daniel Ross</h1>
      <p class="contact-title">General Manager</p>

      <address class="addresses" style="font-style:normal">
        14 Harbor View Ave.<br>Easton, CT 06612
        <div class="address-divider"></div>
        418 River Bend St.<br>Milford, CT 06460
      </address>

      <ul class="channels">
        <li>
          <svg viewBox="0 0 24 24"><path d="M6.6 10.8a15.1 15.1 0 0 0 6.6 6.6l2.2-2.2c.3-.3.7-.4 1-.2 1.1.4 2.3.6 3.6.6.6 0 1 .4 1 1V20c0 .6-.4 1-1 1A17 17 0 0 1 3 4c0-.6.4-1 1-1h3.5c.6 0 1 .4 1 1 0 1.3.2 2.5.6 3.6.1.3 0 .7-.2 1z"/></svg>
          (555) 214-3307
        </li>
        <li>
          <svg viewBox="0 0 24 24"><path d="M7 1h10a2 2 0 0 1 2 2v18a2 2 0 0 1-2 2H7a2 2 0 0 1-2-2V3a2 2 0 0 1 2-2zm0 3v14h10V4zm5 15.5a1 1 0 1 0 0 2 1 1 0 0 0 0-2z"/></svg>
          (555) 386-1142
        </li>
        <li>
          <svg viewBox="0 0 24 24"><path d="M2 5h20v14H2zm2 2v.5l8 5 8-5V7zm0 2.8V17h16V9.8l-8 5z"/></svg>
          danielr@brandonsappliances.com
        </li>
        <li>
          <svg viewBox="0 0 24 24"><path d="M12 2a10 10 0 1 0 0 20 10 10 0 0 0 0-20zm6.9 9h-3a15 15 0 0 0-1.3-5.6A8 8 0 0 1 18.9 11zM12 4.1c.9 1.2 1.8 3.6 1.9 6.9h-3.8c.1-3.3 1-5.7 1.9-6.9zM9.4 5.4A15 15 0 0 0 8.1 11h-3a8 8 0 0 1 4.3-5.6zM5.1 13h3a15 15 0 0 0 1.3 5.6A8 8 0 0 1 5.1 13zm6.9 6.9c-.9-1.2-1.8-3.6-1.9-6.9h3.8c-.1 3.3-1 5.7-1.9 6.9zm2.6-1.3a15 15 0 0 0 1.3-5.6h3a8 8 0 0 1-4.3 5.6z"/></svg>
          www.brandonsappliances.com
        </li>
      </ul>
    </div>

    <p class="back-wordmark">Brandon's Appliances</p>
  </section>

</main>
</body>
</html>
```